Powerpoint Template Background Design

We are looking to update our powerpoint background to align better with our recently updated logo. I've included our current logo (BankGothic Md BT Medium) and previous ppt background we had used for reference. Page orientation should be landscape. Should be usable online and as a printable deck. We are in the digital advertising sales industry and represent various digital ad products to ad agencies and clients who are interested in marketing their products using mobile advertising tools. the RGB color yellow in our logo is 245, 191,34 #fsbf22. We like to also see the grey and black in our logo included. We'd like it to be similar but new and refreshed from our previous ppt background. I've added our current sales deck for your review and consideration with your design.

Target Market(s)

Advertisers, Ad agencies

Industry/Entity Type

Advertising

Colors
ffc214

Requirements
Must have
• Include Logo. Preferably our 3d logo on the cover page. color scheme should match our logo. Must have cover page and template border page that we will use throughout the entire presentation.
Nice to have
• Full cover page graphic using our 3d logo and allows us to add text in a fixed area of the slide
Should not have
• If recommending full slide color/imagery please note it will be used both online and as a printable deck. Do not include the tagline and/or text from the previously used presentation template.

```html
<!DOCTYPE html>
<html lang="en">
<head>
<meta charset="utf-8">
<title>Brightpole Interactive Media – Presentation Template</title>
<link href="https://fonts.googleapis.com/css2?family=Open+Sans:wght@400;600;700&display=swap" rel="stylesheet">
<style>
:root{
  --backdrop:#d9d9d9;
  --yellow:#f5bf22;
  --gold:#b48a0e;
  --gold-deep:#9c7608;
  --ink:#2b2b2b;
  --grey:#6b6b6b;
  --rule:#c9c9c9;
  --white:#ffffff;
}
*{box-sizing:border-box;margin:0;padding:0}
html,body{width:1200px;height:1037px;overflow:hidden}
body{background:var(--backdrop);font-family:"Open Sans",Arial,sans-serif;position:relative;color:var(--ink)}
.slide{position:absolute;width:499px;height:281px;background:var(--white);overflow:hidden;box-shadow:0 1px 3px rgba(0,0,0,.18)}
.col-l{left:83px}.col-r{left:620px}
.row-1{top:60px}.row-2{top:381px}.row-3{top:695px}
.abs{position:absolute}

.slide-title{position:absolute;left:0;top:10px;height:20px;display:flex;align-items:center}
.slide-title::before{content:"";width:6px;height:20px;background:var(--yellow);margin-right:12px}
.slide-title h2{font-size:11.5px;font-weight:700;letter-spacing:.1px;color:var(--ink)}

.footer{position:absolute;left:18px;right:0;bottom:8px;height:14px;display:flex;align-items:center}
.footer .mark{width:8px;height:8px;border-radius:50%;background:var(--yellow);margin-right:5px}
.footer .brand{font-size:5.5px;color:var(--grey);margin-right:8px;white-space:nowrap}
.footer .rule{flex:1;height:1px;background:var(--rule)}
.footer .page{width:19px;height:11px;background:var(--yellow);font-size:7px;font-weight:700;color:var(--ink);display:flex;align-items:center;justify-content:center}

.photo{position:absolute}

/* cover */
.cover .photo{inset:0;background:linear-gradient(120deg,#b48a1a 0%,#c9a640 35%,#8e8a58 65%,#5f7f86 100%)}
.cover .logo-tab{position:absolute;left:28px;top:0;width:96px;height:75px;background:var(--white);border-radius:0 0 12px 12px;display:flex;align-items:center;justify-content:center;gap:4px}
.logo-tab .mark{width:9px;height:9px;border-radius:50%;background:var(--yellow)}
.logo-tab .name{font-size:9px;font-weight:700;letter-spacing:.6px;color:var(--ink)}
.cover .title-block{position:absolute;right:66px;top:206px;text-align:right;color:var(--white)}
.cover .title-block h1{font-size:18px;font-weight:600;line-height:1.2}
.cover .title-block p{font-size:8.5px;font-weight:700}
.cover .divider{position:absolute;left:448px;top:189px;width:2px;height:60px;background:var(--white)}

/* slide 2 */
.intro .textbox{left:28px;top:62px;width:184px;height:184px;background:var(--gold);color:var(--white);font-size:6.1px;line-height:1.45;padding:22px 36px 0 30px}
.intro .photo{left:212px;top:62px;width:260px;height:184px;background:linear-gradient(135deg,#8a5a2e,#b9854d 45%,#ddd6cc 75%,#f0f0f0)}

/* team */
.team-row{position:absolute;top:76px;left:0;right:0;display:flex;justify-content:center;gap:36px}
.member{width:80px;text-align:center}
.member .avatar{width:72px;height:72px;border-radius:50%;margin:0 auto 12px;background:radial-gradient(circle at 50% 40%,#d8d8d8,#8b8b8b 70%,#5a5a5a)}
.member h3{font-size:8.5px;font-weight:700;color:var(--gold)}
.member p{font-size:6.5px;color:var(--grey)}
.team .body{left:40px;right:40px;top:193px;font-size:5.2px;line-height:1.45;color:var(--grey);text-align:center}

/* features */
.features .band{left:0;top:43px;width:283px;height:207px;background:var(--gold)}
.features .photo{left:283px;top:43px;width:216px;height:207px;background:linear-gradient(180deg,#d7d4cf,#a8a29a 45%,#6e675f)}
.features .lead{left:34px;top:84px;width:88px;color:var(--white);font-size:8px;font-weight:700;line-height:1.4;text-align:center}
.features .card{left:141px;top:90px;width:331px;height:120px;background:var(--white);display:flex;justify-content:space-around;align-items:center;padding:0 12px}
.feature{text-align:center}
.feature svg{width:22px;height:22px;display:block;margin:0 auto 8px}
.feature span{font-size:8.5px;font-weight:700;color:var(--ink)}

/* section */
.section .photo{left:0;top:53px;width:499px;height:196px;background:linear-gradient(90deg,#4b5565,#7a8596 45%,#b3bac5 70%,#5b6473)}
.section .panel{left:42px;top:53px;width:184px;height:196px;background:var(--gold);color:var(--white);padding:28px 18px 0 19px}
.section h3{font-size:12px;font-weight:700;margin-bottom:8px}
.section .panel p{font-size:5.2px;line-height:1.45}

/* contact */
.contact h2{position:absolute;left:31px;top:26px;font-size:12px;font-weight:700}
.contact .accent{left:0;top:24px;width:6px;height:22px;background:var(--yellow)}
.region{position:absolute;left:32px;width:100px}
.region h4{font-size:6.4px;font-weight:700;color:var(--gold);margin-bottom:6px}
.region p{font-size:5.2px;line-height:1.4;color:var(--ink)}
.contact .logo{left:32px;top:212px;display:flex;align-items:center;gap:4px}
.contact .logo .mark{width:9px;height:9px;border-radius:50%;background:var(--yellow)}
.contact .logo .name{font-size:9px;font-weight:700;letter-spacing:.6px}
.contact .legal{left:32px;top:238px;width:250px;font-size:3.6px;line-height:1.35;color:var(--grey)}
.contact .web{right:33px;bottom:20px;font-size:7px;font-weight:700;color:var(--white)}
</style>
</head>
<body>

<section class="slide cover col-l row-1">
  <div class="photo" role="img" aria-label="Team working on a tablet with a golden digital data overlay"></div>
  <div class="logo-tab"><span class="mark"></span><span class="name">BRIGHTPOLE</span></div>
  <div class="divider"></div>
  <div class="title-block"><h1>Edit title here</h1><p>edit subtitle here</p></div>
</section>

<section class="slide intro col-r row-1">
  <div class="slide-title"><h2>EDIT TITLE HERE</h2></div>
  <div class="abs textbox">Lorem ipsum dolor sit amet, consectetur adipiscing elit. Mauris porttitor lectus ac sapien rutrum, vitae commodo neque efficitur. Praesent scelerisque consectetur ante, non luctus lectus tempus id. Donec nulla leo, faucibus nec orci et, condimentum iaculis nisl. Nam pharetra risus tellus, id tempor orci tempor sed. Proin gravida justo vitae diam tempor, non imperdiet est facilisis. Vestibulum vitae vestibulum libero, eget suscipit ligula. Class varius turpis sem, eget vulputate sapien interdum vitae. Suspendisse lobortis mi et augue finibus hendrerit.</div>
  <div class="photo" role="img" aria-label="Overhead view of a business meeting around a wooden table"></div>
  <div class="footer"><span class="mark"></span><span class="brand">Brightpole Interactive Media</span><span class="rule"></span><span class="page">2</span></div>
</section>

<section class="slide team col-l row-2">
  <div class="slide-title"><h2>EDIT TITLE HERE</h2></div>
  <div class="team-row">
    <div class="member"><div class="avatar" role="img" aria-label="Portrait photo of team member"></div><h3>CLARA WYNN</h3><p>General Manager</p></div>
    <div class="member"><div class="avatar" role="img" aria-label="Portrait photo of team member"></div><h3>OWEN HALE</h3><p>Trainer Head</p></div>
    <div class="member"><div class="avatar" role="img" aria-label="Portrait photo of team member"></div><h3>RAVI MENON</h3><p>Finance</p></div>
    <div class="member"><div class="avatar" role="img" aria-label="Portrait photo of team member"></div><h3>LEO BARRETT</h3><p>Senior Trainer</p></div>
  </div>
  <p class="abs body">Lorem ipsum dolor sit amet, consectetur adipiscing elit, sed do eiusmod tempor incididunt ut labore et dolore magna aliqua. Ut enim ad minim veniam, quis nostrud exercitation ullamco laboris nisi ut aliquip ex ea commodo consequat. Duis aute irure dolor in reprehenderit in voluptate velit esse cillum dolore eu fugiat nulla pariatur. Excepteur sint occaecat cupidatat non proident, sunt in culpa qui officia deserunt mollit anim id est laborum.</p>
  <div class="footer"><span class="mark"></span><span class="brand">Brightpole Interactive Media</span><span class="rule"></span><span class="page">3</span></div>
</section>

<section class="slide features col-r row-2">
  <div class="slide-title"><h2>EDIT TITLE HERE</h2></div>
  <div class="abs band"></div>
  <div class="photo" role="img" aria-label="Bright open-plan office with city view"></div>
  <p class="abs lead">Lorem ipsum dolor sit amet consectetur adipiscing elit. Cras bibendum mattis leo, ac efficitur ipsum lobortis non. Praesent vitae pulvinar Lorem ipsum dolor sit amet consectetur adipiscing elit. Cras bibendum mattis leo.</p>
  <div class="abs card">
    <div class="feature">
      <svg viewBox="0 0 22 22"><g fill="#f5bf22"><rect x="1" y="1" width="9" height="9"/><rect x="12" y="1" width="9" height="9"/><rect x="1" y="12" width="9" height="9"/><rect x="12" y="12" width="9" height="9"/></g></svg>
      <span>LOREM</span>
    </div>
    <div class="feature">
      <svg viewBox="0 0 22 22"><path fill="#f5bf22" d="M11 2 1 11h3v9h5v-6h4v6h5v-9h3z"/></svg>
      <span>LOREM</span>
    </div>
    <div class="feature">
      <svg viewBox="0 0 22 22"><circle cx="11" cy="11" r="7" fill="none" stroke="#f5bf22" stroke-width="4" stroke-dasharray="3 2.5"/><circle cx="11" cy="11" r="5.5" fill="none" stroke="#f5bf22" stroke-width="2"/></svg>
      <span>LOREM</span>
    </div>
  </div>
  <div class="footer"><span class="mark"></span><span class="brand">Brightpole Interactive Media</span><span class="rule"></span><span class="page">4</span></div>
</section>

<section class="slide section col-l row-3">
  <div class="slide-title"><h2>EDIT TITLE HERE</h2></div>
  <div class="photo" role="img" aria-label="Night city skyline with glowing network connection lines"></div>
  <div class="abs panel">
    <h3>LOREM IPSUM</h3>
    <p>Lorem ipsum dolor sit amet, consectetur adipiscing elit, sed do eiusmod tempor incididunt ut labore et dolore magna aliqua. Ut enim ad minim veniam, quis nostrud exercitation ullamco laboris nisi ut aliquip ex ea commodo consequat. Duis aute irure dolor in reprehenderit in voluptate velit esse cillum dolore eu fugiat nulla pariatur. Excepteur sint occaecat cupidatat non proident, sunt in culpa qui officia deserunt mollit anim id est laborum. Lorem ipsum dolor sit amet, consectetur adipiscing elit, sed do eiusmod tempor incididunt ut labore et dolore magna aliqua. Ut enim ad minim veniam, quis nostrud exercitation ullamco laboris nisi ut aliquip ex ea commodo consequat. Duis aute irure dolor in reprehenderit in voluptate velit esse cillum dolore eu fugiat nulla pariatur. Excepteur sint occaecat cupidatat non proident, sunt in culpa qui officia deserunt mollit anim id est laborum.</p>
  </div>
</section>

<section class="slide contact col-r row-3">
  <svg class="abs" style="left:0;top:0" width="499" height="281" viewBox="0 0 499 281" aria-hidden="true">
    <defs>
      <linearGradient id="skyline" x1="0" y1="0" x2="0" y2="1">
        <stop offset="0" stop-color="#6f9cc4"/><stop offset=".55" stop-color="#a9c2b4"/><stop offset="1" stop-color="#5f8a3e"/>
      </linearGradient>
    </defs>
    <polygon points="235,0 499,0 499,281 390,281" fill="url(#skyline)" role="img" aria-label="City skyline with wireless connectivity icons"/>
    <polygon points="275,281 499,165 499,281" fill="#f5bf22"/>
  </svg>
  <div class="abs accent"></div>
  <h2>Contact us</h2>
  <div class="region" style="top:74px"><h4>United States</h4><p>Lorem ipsum dolor sit amet, consectetur adipiscing elit. Mauris porttitor lect</p></div>
  <div class="region" style="top:135px"><h4>Europe</h4><p>Lorem ipsum dolor sit amet, consectetur adipiscing elit. Mauris porttitor lect</p></div>
  <div class="abs logo"><span class="mark"></span><span class="name">BRIGHTPOLE</span></div>
  <p class="abs legal">Copyright 2018. All rights reserved. No part of this document may be reproduced or stored in a retrieval system without the written permission of Brightpole Interactive Media. All trademarks mentioned herein are the property of their respective owners.</p>
  <p class="abs web">www.brightpolemedia.com</p>
</section>

</body>
</html>
```